Stationary Design Letterhead and Envelope

Artist should provide Letterhead and envelop stationary designs

Info for stationary:
Fernhallow Outdoor Advertising
4873 Quarry Rd. 915 N. PO BOX 528617
Austin, TX 78519

Dale Fernhallow
President
555-862-1907
dale@fernhallowsigns.example
fernhallowsigns.example

Target Market(s)

clients

Colors
0054AA
0677BA
7BADD7
CADEEF
E8F1F8

Requirements
Must have
• high quality unique eye catching and dynamic

```html
<!DOCTYPE html>
<html lang="en">
<head>
<meta charset="utf-8">
<title>Fernhallow Outdoor Advertising – Stationery</title>
<link href="https://fonts.googleapis.com/css2?family=Lato:wght@400;700&display=swap" rel="stylesheet">
<style>
  :root {
    --brand-blue: #0f6fae;
    --accent-blue: #0677BA;
    --rule-blue: #7BADD7;
    --ink: #111111;
    --text: #4a4a4a;
    --paper: #ffffff;
    --backdrop: #e6e8ea;
  }
  * { margin: 0; padding: 0; box-sizing: border-box; }
  html, body { width: 1200px; height: 1200px; overflow: hidden; }
  body { background: var(--backdrop); font-family: "Lato", Arial, sans-serif; color: var(--text); position: relative; }

  .letterhead, .envelope-front, .envelope-back {
    position: absolute; background: var(--paper);
    box-shadow: 0 4px 14px rgba(0,0,0,0.18);
  }
  .letterhead { left: 118px; top: 243px; width: 557px; height: 714px; }
  .envelope-front { left: 714px; top: 457px; width: 432px; height: 216px; }
  .envelope-back { left: 717px; top: 707px; width: 429px; height: 214px; }

  .edge-stripe { position: absolute; left: 0; top: 0; height: 100%; }

  .wordmark { position: absolute; text-align: center; color: var(--brand-blue); font-weight: 700; line-height: 1; }
  .wordmark .mark-square { display: inline-block; background: var(--brand-blue); vertical-align: middle; }
  .letterhead .wordmark { left: 0; width: 100%; top: 24px; font-size: 26px; letter-spacing: 0.5px; }
  .letterhead .wordmark .mark-square { width: 14px; height: 14px; margin-right: 8px; }
  .wordmark .tagline { display: block; font-size: 10.5px; letter-spacing: 1px; margin-top: 5px; }

  .letter-body { position: absolute; left: 53px; top: 130px; width: 450px; font-size: 8.8px; line-height: 1.25; }
  .issue-date { margin-bottom: 12px; }
  .recipient { margin-bottom: 30px; }
  .salutation { margin-bottom: 22px; }
  .letter-body p.para { text-align: justify; line-height: 16px; margin-bottom: 16px; }
  .closing { margin-top: 30px; }
  .signature { width: 130px; height: 16px; margin: 8px 0 10px; background: linear-gradient(90deg, #ececec, #f6f6f6); }
  .signer-name { font-size: 11.5px; color: #333; }
  .signer-title { margin-top: 6px; }

  .letter-footer { position: absolute; left: 53px; width: 450px; top: 654px; text-align: center; }
  .contact-line { font-size: 10.5px; color: #333; }
  .contact-line b { color: var(--accent-blue); font-weight: 700; }
  .footer-rule { display: flex; align-items: center; gap: 4px; margin-top: 6px; color: var(--accent-blue); font-size: 10.5px; }
  .footer-rule::before, .footer-rule::after { content: ""; flex: 1; height: 1px; background: var(--rule-blue); }
  .footer-address { font-size: 10.5px; color: #333; margin-top: 1px; }

  .envelope-front .wordmark { left: 27px; top: 25px; font-size: 15px; text-align: left; }
  .envelope-front .wordmark .mark-square { width: 9px; height: 9px; margin-right: 5px; }
  .envelope-front .wordmark .tagline { font-size: 6.4px; margin-top: 4px; }
  .return-rule { position: absolute; left: 27px; width: 380px; top: 182px; height: 1px; background: #999; }
  .return-address { position: absolute; left: 27px; top: 186px; font-size: 7.6px; line-height: 10px; color: #333; }
  .return-address .return-name { color: var(--accent-blue); }
</style>
</head>
<body>

<section class="letterhead">
  <svg class="edge-stripe" width="13" height="714" viewBox="0 0 13 714">
    <polygon points="0,0 13,0 13,334 0,318" fill="var(--brand-blue)"/>
    <polygon points="0,326 13,343 13,714 0,714" fill="var(--ink)"/>
  </svg>

  <div class="wordmark"><span class="mark-square"></span>FERNHALLOW<span class="tagline">OUTDOOR ADVERTISING</span></div>

  <div class="letter-body">
    <p class="issue-date">Issuing Date: May 5, 2018</p>
    <p class="recipient">Name Of Employee Mr. XYZABC<br>Address of Employee<br>Address Line 2 etc..</p>
    <p class="salutation">Dear Mr.XYZABC</p>
    <p class="para">Lorem Ipsum has been the industry's standard dummy text ever since the 1500s, when an unknown printer took a galley of type and scrambled it to make a type specimen book. It has survived not only five centuries, but also the leap into electronic typesetting, remaining essentially unchanged. It was popularised in the 1960s with the release of Letraset sheets containing Lorem Ipsum passages, and more recently with desktop publishing software like Aldus PageMaker including versions of Lorem Ipsum.</p>
    <p class="para">Lorem Ipsum is simply dummy text of the printing and typesetting industry. Lorem Ipsum has been the industry's standard dummy text ever since the 1500s, when an unknown printer took a galley of type and scrambled it to make a type specimen book.</p>
    <p class="para">It has survived not only five centuries, but also the leap into electronic typesetting, remaining essentially unchanged. It was popularised in the 1960s with the release of Letraset sheets containing Lorem IpsumIpsum passages.</p>
    <p class="closing">Yours Sincerely</p>
    <div class="signature" role="img" aria-label="Handwritten signature of the managing director"></div>
    <p class="signer-name">Martin Alcott</p>
    <p class="signer-title">Managing Director</p>
  </div>

  <footer class="letter-footer">
    <p class="contact-line"><b>P:</b> 555-862-1907 &nbsp;|&nbsp; <b>E:</b> dale@fernhallowsigns.example &nbsp;|&nbsp; <b>W:</b> fernhallowsigns.example</p>
    <p class="footer-rule">Fernhallow Outdoor Advertising</p>
    <p class="footer-address">4873 Quarry Rd. 915 N. PO BOX 528617, Austin, TX 78519</p>
  </footer>
</section>

<section class="envelope-front">
  <svg class="edge-stripe" width="7" height="216" viewBox="0 0 7 216">
    <polygon points="0,0 7,0 7,112 0,104" fill="var(--brand-blue)"/>
    <polygon points="0,110 7,119 7,216 0,216" fill="var(--ink)"/>
  </svg>
  <div class="wordmark"><span class="mark-square"></span>FERNHALLOW<span class="tagline">OUTDOOR ADVERTISING</span></div>
  <div class="return-rule"></div>
  <p class="return-address"><span class="return-name">Fernhallow Outdoor Advertising</span><br>4873 Quarry Rd. 915 N. PO BOX 528617, Austin, TX 78519</p>
</section>

<section class="envelope-back">
  <svg width="429" height="52" viewBox="0 0 429 52" style="position:absolute;left:0;top:0">
    <polygon points="0,0 429,0 413,51 16,51" fill="var(--brand-blue)"/>
  </svg>
</section>

</body>
</html>
```